VARNOK PTY LTD - Business Cards

Design a modern business card - using the attached Designs.
Same design as on the front, apart from the names/numbers/emails to be different.
We want the cards to be very glossy to stand out, do I think the simple black/white/metallic will be effective.
Both lots of details below:

Kyle Fornaby
Director
kyle_varnok@quillnet.example
0491 382 604

Martin Slade
Director
marty_varnok@quillnet.example
0418 305 249

```html
<!DOCTYPE html>
<html lang="en">
<head>
<meta charset="utf-8">
<title>VARNOK PTY LTD – Business Cards</title>
<link href="https://fonts.googleapis.com/css2?family=Open+Sans:wght@400;600;700&display=swap" rel="stylesheet">
<style>
  :root {
    --page: #ffffff;
    --band: rgba(30, 30, 30, 0.85);
    --strip: rgba(40, 40, 40, 0.6);
    --strip-line: rgba(220, 220, 220, 0.55);
    --text-light: #ffffff;
    --text-muted: #8a8a8a;
    --text-phone: #9e9e9e;
    --mark-dark: #1c1c1c;
    --bolt: #5a5a5a;
  }
  html, body {
    margin: 0;
    width: 1200px;
    height: 1000px;
    overflow: hidden;
    background: var(--page);
  }
  .sheet { position: relative; width: 1200px; height: 1000px; }
  .card {
    position: absolute;
    left: 336px;
    width: 454px;
    height: 265px;
    filter: drop-shadow(3px 4px 4px rgba(0,0,0,0.45));
  }
  .card--front { top: 59px; }
  .card--martin { top: 362px; }
  .card--kyle { top: 671px; }
  .card svg { display: block; font-family: "Open Sans", sans-serif; }
  .wordmark { font-weight: 700; letter-spacing: 1px; }
  .wordmark--dark { fill: var(--mark-dark); }
  .wordmark--light { fill: var(--text-light); }
  .name { fill: var(--text-light); font-size: 16px; }
  .role { fill: var(--text-muted); font-size: 8px; }
  .email { fill: var(--text-muted); font-size: 10.5px; }
  .phone { fill: var(--text-phone); font-size: 15px; font-weight: 600; }
  .service { fill: var(--text-light); font-size: 8.5px; }
  .bolt { fill: var(--bolt); stroke: #2a2a2a; stroke-width: 1; }
</style>
</head>
<body>
<div class="sheet">

  <svg width="0" height="0" style="position:absolute">
    <defs>
      <linearGradient id="carbonFill" x1="0" y1="0" x2="1" y2="1">
        <stop offset="0" stop-color="#1e1e1e"/>
        <stop offset="0.5" stop-color="#2b2b2b"/>
        <stop offset="1" stop-color="#0c0c0c"/>
      </linearGradient>
      <linearGradient id="metalFill" x1="0" y1="0" x2="0" y2="1">
        <stop offset="0" stop-color="#5a5a5a"/>
        <stop offset="0.35" stop-color="#d6d6d6"/>
        <stop offset="0.6" stop-color="#a8a8a8"/>
        <stop offset="1" stop-color="#3e3e3e"/>
      </linearGradient>
      <linearGradient id="metalSide" x1="0" y1="0" x2="0" y2="1">
        <stop offset="0" stop-color="#777"/>
        <stop offset="0.18" stop-color="#cfcfcf"/>
        <stop offset="0.5" stop-color="#6a6a6a"/>
        <stop offset="0.85" stop-color="#bdbdbd"/>
        <stop offset="1" stop-color="#555"/>
      </linearGradient>
    </defs>
  </svg>

  <!-- Front -->
  <div class="card card--front">
    <svg width="454" height="265" viewBox="0 0 454 265">
      <rect width="454" height="265" fill="url(#carbonFill)" role="img" aria-label="Dark carbon-fibre texture"/>
      <rect x="109" y="0" width="229" height="265" fill="url(#metalFill)" role="img" aria-label="Brushed metal plate"/>
      <circle class="bolt" cx="123" cy="15" r="4"/>
      <circle class="bolt" cx="327" cy="15" r="4"/>
      <circle class="bolt" cx="123" cy="253" r="4"/>
      <circle class="bolt" cx="327" cy="253" r="4"/>
      <text class="wordmark wordmark--dark" x="224" y="139" font-size="21" text-anchor="middle">VARNOK PTY LTD</text>
    </svg>
  </div>

  <!-- Back: Martin Slade -->
  <div class="card card--martin">
    <svg width="454" height="265" viewBox="0 0 454 265">
      <rect width="454" height="265" fill="url(#carbonFill)" role="img" aria-label="Dark carbon-fibre texture"/>
      <polygon points="0,0 294,0 199,265 0,265" fill="url(#metalSide)" role="img" aria-label="Brushed metal panel"/>
      <polygon points="0,48 277,48 245,136 0,136" fill="var(--band)"/>
      <line x1="0" y1="48" x2="277" y2="48" stroke="#e6e6e6" stroke-width="1.5"/>
      <g fill="var(--strip)">
        <rect x="0" y="153" width="258" height="11"/>
        <rect x="0" y="165" width="252" height="11"/>
        <rect x="0" y="177" width="248" height="11"/>
        <rect x="0" y="189" width="244" height="11"/>
        <rect x="0" y="201" width="240" height="11"/>
      </g>
      <g stroke="var(--strip-line)" stroke-width="0.8">
        <line x1="0" y1="153" x2="258" y2="153"/>
        <line x1="0" y1="165" x2="252" y2="165"/>
        <line x1="0" y1="177" x2="248" y2="177"/>
        <line x1="0" y1="189" x2="244" y2="189"/>
        <line x1="0" y1="201" x2="240" y2="201"/>
      </g>
      <text class="name" x="52" y="79">Martin Slade</text>
      <text class="role" x="52" y="89">Director</text>
      <text class="email" x="52" y="99">marty_varnok@quillnet.example</text>
      <text class="phone" x="52" y="117">0418 305 249</text>
      <text class="service" x="53" y="162">Labour Hire</text>
      <text class="service" x="53" y="174">Machine Shutdowns</text>
      <text class="service" x="53" y="186">Preventative Maintence and Servicing</text>
      <text class="service" x="53" y="198">Breakdown Repairs</text>
      <text class="service" x="53" y="210">Contract Supervision</text>
      <text class="wordmark wordmark--light" x="353" y="138" font-size="16" text-anchor="middle">VARNOK PTY LTD</text>
    </svg>
  </div>

  <!-- Back: Kyle Fornaby -->
  <div class="card card--kyle">
    <svg width="454" height="265" viewBox="0 0 454 265">
      <rect width="454" height="265" fill="url(#carbonFill)" role="img" aria-label="Dark carbon-fibre texture"/>
      <polygon points="0,0 294,0 199,265 0,265" fill="url(#metalSide)" role="img" aria-label="Brushed metal panel"/>
      <polygon points="0,48 277,48 245,136 0,136" fill="var(--band)"/>
      <line x1="0" y1="48" x2="277" y2="48" stroke="#e6e6e6" stroke-width="1.5"/>
      <g fill="var(--strip)">
        <rect x="0" y="153" width="258" height="11"/>
        <rect x="0" y="165" width="252" height="11"/>
        <rect x="0" y="177" width="248" height="11"/>
        <rect x="0" y="189" width="244" height="11"/>
        <rect x="0" y="201" width="240" height="11"/>
      </g>
      <g stroke="var(--strip-line)" stroke-width="0.8">
        <line x1="0" y1="153" x2="258" y2="153"/>
        <line x1="0" y1="165" x2="252" y2="165"/>
        <line x1="0" y1="177" x2="248" y2="177"/>
        <line x1="0" y1="189" x2="244" y2="189"/>
        <line x1="0" y1="201" x2="240" y2="201"/>
      </g>
      <text class="name" x="52" y="79">Kyle Fornaby</text>
      <text class="role" x="52" y="89">Director</text>
      <text class="email" x="52" y="99">kyle_varnok@quillnet.example</text>
      <text class="phone" x="52" y="117">0491 382 604</text>
      <text class="service" x="53" y="162">Labour Hire</text>
      <text class="service" x="53" y="174">Machine Shutdowns</text>
      <text class="service" x="53" y="186">Preventative Maintence and Servicing</text>
      <text class="service" x="53" y="198">Breakdown Repairs</text>
      <text class="service" x="53" y="210">Contract Supervision</text>
      <text class="wordmark wordmark--light" x="353" y="138" font-size="16" text-anchor="middle">VARNOK PTY LTD</text>
    </svg>
  </div>

</div>
</body>
</html>
```